Business card design for new, innovative company - BluePlinth

We are a new company looking for a business card design that is fun, different and quirky. Must use corporate colour green - CMYK C:55, M:0, Y:100, K:0, and corporate colour grey - C:0, M:0, Y: 0, K:70.

We have developed the first real time data application, in which people are able to profile the data of their existing customers in order to pull out more good fit clients to direct their marketing activities at.

Industry/Entity Type

Marketing

Requirements
Must have
• Logo, name, title, telephone number, fax number, email, website, address

```html
<!DOCTYPE html>
<html lang="en">
<head>
<meta charset="utf-8">
<title>BluePlinth Business Card</title>
<link rel="stylesheet" href="https://fonts.googleapis.com/css2?family=Montserrat:wght@400;700&display=swap">
<style>
  :root {
    --brand-green: #7ed321;
    --brand-grey: #6d6e71;
    --grey-dark: #55575a;
    --card-black: #050505;
    --text-white: #ffffff;
    --page-bg: #e9e9e7;
  }
  * { box-sizing: border-box; margin: 0; padding: 0; }
  html, body {
    width: 1200px; height: 1000px; overflow: hidden;
    background: var(--page-bg);
    font-family: "Montserrat", Arial, sans-serif;
  }
  .stage { position: relative; width: 1200px; height: 1000px; }

  .card {
    position: absolute;
    width: 720px; height: 420px;
    border-radius: 34px;
    overflow: hidden;
    box-shadow: 0 10px 26px rgba(0,0,0,0.25);
  }

  /* Front */
  .card-front { left: 80px; top: 50px; }
  .front-pattern {
    position: absolute; inset: 0;
    background: radial-gradient(ellipse at 55% 45%, #7a7b7e 0%, var(--brand-grey) 55%, var(--grey-dark) 100%);
  }
  .front-name {
    position: absolute; left: 118px; top: 212px;
    font-weight: 700; font-size: 76px; letter-spacing: -4px;
    color: var(--brand-green); line-height: 1;
  }

  /* Back */
  .card-back { left: 400px; top: 530px; background: var(--card-black); }
  .back-name {
    position: absolute; left: 70px; top: 60px;
    font-weight: 700; font-size: 58px; letter-spacing: -3px;
    color: var(--brand-green); line-height: 1;
  }
  .address { position: absolute; left: 60px; top: 220px; color: var(--text-white); }
  .address-heading {
    color: var(--brand-green); font-weight: 700; font-size: 23px; margin-bottom: 14px;
  }
  .address-lines { font-size: 16px; line-height: 22px; font-style: normal; }

  .contact { position: absolute; right: 62px; top: 280px; text-align: right; color: var(--text-white); }
  .contact-name { color: var(--brand-green); font-weight: 700; font-size: 25px; margin-bottom: 14px; }
  .contact-list { list-style: none; font-size: 15px; line-height: 21px; }
  .contact-list li { display: flex; justify-content: flex-end; align-items: center; gap: 8px; }
  .contact-icon { width: 12px; height: 12px; flex: none; }
</style>
</head>
<body>
<main class="stage">

  <section class="card card-front" aria-label="Card front">
    <div class="front-pattern" role="img" aria-label="Grey background with a grid of embossed rounded squares"></div>
    <div class="front-name">BluePlinth</div>
  </section>

  <section class="card card-back" aria-label="Card back">
    <div class="back-name">BluePlinth</div>

    <div class="address">
      <h2 class="address-heading">Address</h2>
      <address class="address-lines">
        22a Fenmoor Road,<br>
        Ely,<br>
        Cambridgeshire,<br>
        CB7 4QT
      </address>
    </div>

    <div class="contact">
      <h2 class="contact-name">Jenna Carlisle</h2>
      <ul class="contact-list">
        <li>07700900418
          <svg class="contact-icon" viewBox="0 0 12 12" aria-hidden="true"><rect x="0.5" y="0.5" width="11" height="11" rx="2" fill="none" stroke="#7ed321"/><rect x="4" y="2.5" width="4" height="7" rx="0.8" fill="#7ed321"/></svg>
        </li>
        <li>01632 960735
          <svg class="contact-icon" viewBox="0 0 12 12" aria-hidden="true"><rect x="0.5" y="0.5" width="11" height="11" rx="2" fill="none" stroke="#7ed321"/><path d="M3.5 3 L5 3 L5.5 4.5 L4.8 5.2 Q5.6 6.6 6.8 7.2 L7.5 6.5 L9 7 L9 8.5 Q5 9 3.5 3Z" fill="#7ed321"/></svg>
        </li>
        <li>jenna.carlisle@plinthdata.com
          <svg class="contact-icon" viewBox="0 0 12 12" aria-hidden="true"><rect x="0.5" y="0.5" width="11" height="11" rx="2" fill="none" stroke="#7ed321"/><rect x="2.5" y="3.5" width="7" height="5" fill="none" stroke="#7ed321"/><path d="M2.5 3.5 L6 6.5 L9.5 3.5" fill="none" stroke="#7ed321"/></svg>
        </li>
        <li>www.blueplinth.com
          <svg class="contact-icon" viewBox="0 0 12 12" aria-hidden="true"><rect x="0.5" y="0.5" width="11" height="11" rx="2" fill="none" stroke="#7ed321"/><circle cx="6" cy="6" r="3.5" fill="none" stroke="#7ed321"/><path d="M2.5 6 H9.5 M6 2.5 V9.5" stroke="#7ed321"/></svg>
        </li>
      </ul>
    </div>
  </section>

</main>
</body>
</html>
```